Brightmill Kitchens sell sheet

Make a 2 sided large format post card (5.5 x 8.5 inches) that introduces Brightmill Kitchens to prospective customers. Use the images and leave space for main selling points on front. Then leave space for a map and further details on the back.
PLEASE INCLUDE THE FOLLOWING CONTENT:
MAIN PAGE
heading:
Contract manufacturing & 3PL in Metro NYC
bullets:
Modern conveniently located facility with multiple lines. SQF, Kosher, Non-GMO, Organic, Gluten-Free.
Slabbing, single and coextrusion, baking, liquid & dry blending & filling.
3PL warehousing & fulfillment
BACK PAGE:
BrightMill Kitchens was created and is operated by experienced, successful natural food brand owners, as a higher-level contract manufacturing experience. Our goal is to provide the control and cost structure of self-manufacturing, while leveraging our capital investment and expertise.
You're always welcome to collaborate with us, observe your production and to enjoy our on-site fitness center, yoga classes, meditation, nursing and telework facilities.
Contact Owen Halvorsen 914-555-0163 owen@brightmill.example
Return address for postcard, should be small:
48 Larkspur Lane #517, Danbury CT 06811
Target Market(s)
B to B. We are an industrial contract manufacturer doing large volume production.
Industry/Entity Type
We design and manufacture natural food products for other companies to sell under their own brands.
Requirements
Must have
- Leave a small but adequate area for the postcard to be mailed. Must depict the some elements of all product stock images provided. Showing the full variety of food bars and product pouches and bottles we package so they are recognizable at a glance. The bar with the filling is not the major product, so even though it has it's own image, the other bars should be more prominent.
Nice to have
- A map same or similar to the one shown. The circle depicts the necessary visible radius. It can also be rectangular.

```html
<!DOCTYPE html>
<html lang="en">
<head>
<meta charset="utf-8">
<title>Brightmill Kitchens Postcard</title>
<link href="https://fonts.googleapis.com/css2?family=Montserrat:wght@300;400;700&family=Roboto+Condensed:wght@300;400&family=Arimo:wght@400;700&display=swap" rel="stylesheet">
<style>
  :root {
    --backdrop: #2b2b2b;
    --paper: #ffffff;
    --coral: #ef4b52;
    --orange: #f59423;
    --yellow: #f3cd21;
    --ink-light: #ffffff;
    --rule: #555555;
  }
  * { margin: 0; padding: 0; box-sizing: border-box; }
  html, body { width: 1200px; height: 465px; overflow: hidden; background: var(--backdrop); }
  .canvas { position: relative; width: 1200px; height: 465px; }
  .card {
    position: absolute; top: 55px; width: 524px; height: 356px;
    background: var(--paper); overflow: hidden;
    font-family: "Montserrat", sans-serif; color: var(--ink-light);
  }
  .card--front { left: 57px; }
  .card--back { left: 619px; }
  .card__shapes { position: absolute; inset: 0; }

  /* front */
  .brand { position: absolute; left: 26px; top: 44px; display: flex; align-items: center; gap: 8px; }
  .brand__dot { width: 30px; height: 30px; border-radius: 50%; background: var(--coral); }
  .brand__name { font-weight: 700; font-size: 15px; line-height: 1.1; color: var(--coral); text-transform: uppercase; letter-spacing: .5px; }
  .headline { position: absolute; left: 14px; top: 174px; font-size: 16.5px; line-height: 21.6px; letter-spacing: 1.6px; }
  .headline__strong { display: block; font-weight: 700; }
  .headline__light { display: block; font-weight: 300; font-size: 17.5px; }
  .front-rule { position: absolute; left: 14px; top: 286px; width: 232px; height: 1px; background: var(--ink-light); }
  .front-copy { position: absolute; left: 14px; top: 290px; width: 232px; font-family: "Arimo", sans-serif; font-size: 5.3px; line-height: 6.4px; }
  .front-copy__lead { font-weight: 700; }
  .web-pill {
    position: absolute; left: 14px; top: 329px; width: 232px; height: 15px; border-radius: 8px;
    background: var(--paper); color: var(--coral); font-size: 6.5px; letter-spacing: 2.4px;
    display: flex; align-items: center; justify-content: center;
  }
  .contact-pill {
    position: absolute; left: 282px; top: 308px; width: 104px; height: 15px; border-radius: 8px;
    border: 1.5px solid var(--paper); font-size: 10px; font-weight: 400;
    display: flex; align-items: center; justify-content: center; letter-spacing: .1px;
  }
  .phone-icon { position: absolute; left: 392px; top: 304px; width: 23px; height: 23px; }
  .phone-number { position: absolute; left: 419px; top: 306px; font-size: 14px; font-weight: 300; letter-spacing: .3px; white-space: nowrap; }

  /* back */
  .services-title { position: absolute; left: 25px; top: 20px; font-size: 15px; font-weight: 400; letter-spacing: .4px; }
  .service { position: absolute; left: 20px; width: 240px; display: flex; gap: 11px; }
  .service__icon { width: 38px; height: 38px; flex: none; }
  .service__title { font-family: "Arimo", sans-serif; font-size: 7.6px; margin-top: 2px; }
  .service__text { font-family: "Arimo", sans-serif; font-size: 5.4px; line-height: 6.6px; margin-top: 2px; width: 130px; }
  .feature-title { position: absolute; left: 15px; top: 232px; font-family: "Roboto Condensed", sans-serif; font-weight: 300; font-size: 28px; line-height: 1; letter-spacing: .3px; }
  .feature-sub { position: absolute; left: 15px; top: 264px; font-family: "Roboto Condensed", sans-serif; font-weight: 300; font-size: 15px; line-height: 1; white-space: nowrap; }
  .feature-copy { position: absolute; left: 15px; width: 236px; font-family: "Arimo", sans-serif; font-size: 5.2px; line-height: 6.3px; }
  .feature-contact { position: absolute; left: 15px; top: 340px; width: 236px; font-family: "Arimo", sans-serif; font-size: 5.2px; line-height: 6.3px; font-weight: 700; }
  .stamp-box { position: absolute; left: 417px; top: 35px; width: 84px; height: 84px; border: 1px dashed var(--rule); }
  .address-line { position: absolute; left: 291px; width: 210px; border-top: 1px dashed var(--rule); }
  .map-area {
    position: absolute; left: 288px; top: 266px; width: 218px; height: 75px;
    border: 2px solid #555; background: linear-gradient(135deg, #eef0ea 0%, #e4e9df 55%, #dfe8d8 100%);
  }
</style>
</head>
<body>
<div class="canvas">

  <!-- FRONT -->
  <section class="card card--front">
    <svg class="card__shapes" viewBox="0 0 524 356" width="524" height="356" aria-hidden="true">
      <defs>
        <linearGradient id="bar-tones" x1="0" y1="0" x2="1" y2="1">
          <stop offset="0" stop-color="#c9a56a"/>
          <stop offset=".5" stop-color="#8a5a3a"/>
          <stop offset="1" stop-color="#d8b77d"/>
        </linearGradient>
        <radialGradient id="pastry-tones" cx=".55" cy=".45" r=".7">
          <stop offset="0" stop-color="#d9b98a"/>
          <stop offset=".6" stop-color="#b98d5c"/>
          <stop offset="1" stop-color="#5a3a2a"/>
        </radialGradient>
      </defs>
      <ellipse cx="97" cy="364" rx="360" ry="228" fill="var(--orange)"/>
      <rect x="250" y="180" width="274" height="176" fill="var(--orange)"/>
      <ellipse cx="80" cy="380" rx="190" ry="230" fill="var(--coral)" stroke="var(--yellow)" stroke-width="5"/>
      <ellipse cx="381" cy="52" rx="202" ry="232" fill="var(--yellow)"/>
      <ellipse cx="381" cy="48" rx="198" ry="228" fill="url(#pastry-tones)" role="img" aria-label="Photo of filled fruit bars with strawberries"/>
      <circle cx="230" cy="200" r="57" fill="var(--paper)"/>
      <circle cx="230" cy="200" r="52" fill="url(#bar-tones)" role="img" aria-label="Photo of assorted granola and protein bars"/>
    </svg>

    <div class="brand">
      <span class="brand__dot"></span>
      <span class="brand__name">Brightmill<br>Kitchens</span>
    </div>

    <h1 class="headline">
      <span class="headline__strong">INTRODUCES</span>
      <span class="headline__strong">BRIGHTMILL</span>
      <span class="headline__strong">KITCHENS TO</span>
      <span class="headline__light">PROSPECTIVE</span>
      <span class="headline__light">CUSTOMERS.</span>
    </h1>
    <div class="front-rule"></div>
    <p class="front-copy"><span class="front-copy__lead">Contract manufacturing &amp; 3PL in Metro NYC.</span> Modern conveniently located facility with multiple lines. SQF, Kosher, Non-GMO, Organic, Gluten-Free. Slabbing, single and coextrusion, baking, liquid &amp; dry blending &amp; filling. 3PL warehousing &amp; fulfillment.</p>
    <div class="web-pill">www.brightmillkitchens.example</div>

    <div class="contact-pill">CONTACTS ABOUT</div>
    <svg class="phone-icon" viewBox="0 0 24 24" aria-hidden="true">
      <circle cx="12" cy="12" r="12" fill="var(--paper)"/>
      <path d="M8.2 5.5c.5-.3 1.1-.2 1.4.3l1.2 2.1c.3.5.2 1-.2 1.4l-.9.8c.6 1.4 1.8 2.7 3.2 3.4l.8-.9c.4-.4 1-.5 1.4-.2l2.1 1.2c.5.3.6.9.3 1.4l-.8 1.3c-.4.6-1.1.9-1.8.7-3.6-1-6.6-4-7.6-7.6-.2-.7.1-1.4.7-1.8z" fill="var(--orange)"/>
    </svg>
    <div class="phone-number">914-555-0163</div>
  </section>

  <!-- BACK -->
  <section class="card card--back">
    <svg class="card__shapes" viewBox="0 0 524 356" width="524" height="356" aria-hidden="true">
      <ellipse cx="42" cy="117" rx="228" ry="262" fill="var(--coral)"/>
      <ellipse cx="80" cy="364" rx="200" ry="154" fill="var(--orange)"/>
    </svg>

    <h2 class="services-title">OUR SERVICES</h2>

    <div class="service" style="top:53px">
      <svg class="service__icon" viewBox="0 0 38 38" aria-hidden="true">
        <circle cx="19" cy="19" r="18" fill="var(--paper)"/>
        <circle cx="19" cy="19" r="14.5" fill="none" stroke="var(--coral)" stroke-width="1.4"/>
        <path d="M19 10.5a6 6 0 0 0-6 6c0 4.3 6 11 6 11s6-6.7 6-11a6 6 0 0 0-6-6z" fill="none" stroke="var(--coral)" stroke-width="1.6"/>
        <circle cx="19" cy="16.5" r="2.2" fill="none" stroke="var(--coral)" stroke-width="1.4"/>
      </svg>
      <div>
        <div class="service__title">MODERN FACILITY</div>
        <p class="service__text">Modern conveniently located facility with multiple lines. SQF, Kosher, Non-GMO, Organic, Gluten-Free.</p>
      </div>
    </div>

    <div class="service" style="top:108px">
      <svg class="service__icon" viewBox="0 0 38 38" aria-hidden="true">
        <circle cx="19" cy="19" r="18" fill="var(--paper)"/>
        <circle cx="19" cy="19" r="14.5" fill="none" stroke="var(--coral)" stroke-width="1.4"/>
        <circle cx="19" cy="19" r="8.5" fill="none" stroke="var(--coral)" stroke-width="1.8"/>
        <path d="M19 11.5v7.5h7.5" fill="none" stroke="var(--coral)" stroke-width="1.8"/>
      </svg>
      <div>
        <div class="service__title">PRODUCTION</div>
        <p class="service__text">Slabbing, single and coextrusion, baking, liquid &amp; dry blending &amp; filling.</p>
      </div>
    </div>

    <div class="service" style="top:162px">
      <svg class="service__icon" viewBox="0 0 38 38" aria-hidden="true">
        <circle cx="19" cy="19" r="18" fill="var(--paper)"/>
        <circle cx="19" cy="19" r="14.5" fill="none" stroke="var(--coral)" stroke-width="1.4"/>
        <circle cx="17" cy="17" r="5.5" fill="none" stroke="var(--coral)" stroke-width="1.8"/>
        <path d="M21 21l5 5" stroke="var(--coral)" stroke-width="2.4" stroke-linecap="round"/>
      </svg>
      <div>
        <div class="service__title">3PL SERVICES</div>
        <p class="service__text">3PL warehousing &amp; fulfillment.</p>
      </div>
    </div>

    <h2 class="feature-title">METRO NYC</h2>
    <div class="feature-sub">CONTRACT MANUFACTURING &amp; 3PL</div>
    <p class="feature-copy" style="top:285px">BrightMill Kitchens was created and is operated by experienced, successful natural food brand owners, as a higher-level contract manufacturing experience. Our goal is to provide the control and cost structure of self-manufacturing, while leveraging our capital investment and expertise.</p>
    <p class="feature-copy" style="top:315px">You're always welcome to collaborate with us, observe your production and to enjoy our on-site fitness center, yoga classes, meditation, nursing and telework facilities.</p>
    <p class="feature-contact">Contact Owen Halvorsen · 914-555-0163 · owen@brightmill.example<br>48 Larkspur Lane #517, Danbury CT 06811</p>

    <div class="stamp-box"></div>
    <div class="address-line" style="top:160px"></div>
    <div class="address-line" style="top:188px"></div>
    <div class="address-line" style="top:217px"></div>
    <div class="address-line" style="top:245px"></div>

    <div class="map-area" role="img" aria-label="Street map of the facility area"></div>
  </section>

</div>
</body>
</html>
```